Law firm website marketed direct to many individual clients

I need someone to design a very basic website for a law firm that will be very eye catching. It's going to be a single-paged, scrolling website with a small number of folds. I have uploaded a simple word document that outlines the basics of what I thought could be the layout, but I am open to suggestion on font, size, shades of color, organization, etc. etc. Essentially the website just needs to be a very efficient and visually appealing way of conveying some simple messages.

Target Market(s)

High volumes of individuals who have gotten into a car accident and then google on their phones a lawyer to hire to represent them.

Industry/Entity Type

Legal

Number of Pages Required

1 page

Font styles to use
Serif
Sans Serif

Colors
34a7d7
85cae6
0592cd

Requirements
Must have
• Must be bright and grab the users attention with color scheme and layout. The different sections should be done in such a way that they can fit entirely onto one smart phone or tablet screen.
Nice to have
• I'd like to try and see what it looks like if in the middle somewhere there is a fold that says "MEET YOUR ATTORNEYS" and includes individual photos of two attorneys, one on the left side and one on the right. And then a small bio section on them. I don't want the photos to include a square or rectangle background, I want the person in the photo to be superimposed on top of whatever pattern or background you have in the fold.
Should not have
• Do not want too much text. Anything more than 2 sentences in any single place is unacceptable.

```html
<!DOCTYPE html>
<html lang="en">
<head>
<meta charset="utf-8">
<title>Harborline Law Group</title>
<link rel="stylesheet" href="https://fonts.googleapis.com/css2?family=Cinzel:wght@400;700&family=Lato:wght@400;700&display=swap">
<style>
:root{
  --blue:#34a7d7;
  --blue-deep:#0592cd;
  --blue-soft:#85cae6;
  --band:#2196cf;
  --ink:#1c1c1c;
  --slate:#353a45;
  --slate-deep:#2b2f38;
  --white:#ffffff;
  --muted:#d6d9de;
}
*{margin:0;padding:0;box-sizing:border-box}
html,body{width:792px;height:1200px;overflow:hidden;background:var(--white)}
body{position:relative;font-family:'Lato',sans-serif;color:var(--ink)}
.abs{position:absolute}
.serif{font-family:'Cinzel',serif}

/* header */
.site-header{left:0;top:0;width:792px;height:53px;background:var(--white);border-bottom:2px solid var(--blue)}
.brand{left:66px;top:16px;display:flex;align-items:center;gap:8px}
.brand-mark{width:20px;height:20px;background:var(--blue-deep)}
.brand-name{font-family:'Cinzel',serif;font-weight:400;font-size:15px;color:var(--blue-deep);letter-spacing:1px}
.header-call{left:590px;top:12px;display:flex;align-items:center;gap:6px}
.header-call small{display:block;font-size:7px;color:var(--blue);letter-spacing:.3px}
.header-call strong{display:block;font-family:'Cinzel',serif;font-weight:400;font-size:17px;color:var(--ink);line-height:1}

/* hero */
.hero{left:0;top:53px;width:792px;height:309px;background:linear-gradient(90deg,#8a3a32 0%,#b89a86 25%,#c9c1b6 45%,#a9a6a4 60%,#3c3f4b 80%,#9a8d84 100%)}
.hero-shade{left:0;top:53px;width:792px;height:309px;background:rgba(30,30,35,.25)}
.hero-kicker{left:0;top:155px;width:792px;text-align:center;color:var(--white);font-weight:700;font-size:14px}
.hero-title{left:0;top:176px;width:792px;text-align:center;color:var(--white);font-family:'Cinzel',serif;font-size:31px;letter-spacing:.5px}
.hero-btn{left:332px;top:230px;width:130px;height:26px;background:var(--blue);display:flex;align-items:center;justify-content:center;gap:5px;color:var(--white);font-size:8px;font-weight:700}
.hero-btn span{font-family:'Cinzel',serif;font-weight:400;font-size:10px}
.slide-tab{left:0;top:197px;width:12px;height:34px;background:rgba(255,255,255,.25);display:flex;flex-direction:column;justify-content:space-around;align-items:center;padding:4px 0}
.slide-tab i{width:3px;height:3px;border-radius:50%;background:var(--white)}
.scroll-cue{left:386px;top:322px}

/* features */
.feature{top:410px;width:180px;text-align:center}
.feature-icon{width:68px;height:68px;margin:0 auto;border-radius:50%;background:radial-gradient(circle at 45% 40%,#fafafa,#dcdcdc 70%,#c4c4c4);border:1px solid #cfcfcf}
.feature-shadow{width:40px;height:2px;margin:6px auto 0;background:linear-gradient(90deg,transparent,#ccc,transparent)}
.feature h3{font-family:'Cinzel',serif;font-weight:400;font-size:10px;color:var(--blue);letter-spacing:.5px;line-height:12px;margin-top:10px;min-height:24px;display:flex;align-items:center;justify-content:center}
.feature p{font-size:8.5px;line-height:9px;margin-top:5px}

/* band */
.cta-band{left:0;top:588px;width:792px;height:72px;background:var(--band)}
.cta-band .bar{left:66px;top:611px;width:2px;height:30px;background:var(--white)}
.cta-band-text{left:77px;top:614px;color:var(--white);font-weight:700;font-size:17px;letter-spacing:.2px}
.cta-band-icon{left:453px;top:606px}
.cta-band-num{left:510px;top:604px;color:var(--white);font-family:'Cinzel',serif;font-size:30px}

/* panels */
.panel-left{left:0;top:660px;width:396px;height:232px;background:linear-gradient(135deg,#3a2a22,#5a3b2c 40%,#2a2626 70%,#4a3a2e)}
.panel-right{left:396px;top:660px;width:396px;height:232px;background:linear-gradient(120deg,#d8dce0,#eef0f1 45%,#cfd3d6 75%,#e7e8e9)}
.panel-box{top:732px;width:310px;height:98px;border:1px dashed rgba(150,150,150,.7);text-align:center}
.panel-box h2{font-family:'Cinzel',serif;font-weight:400;font-size:15px;letter-spacing:.5px;margin:-9px auto 0;padding:0 10px;width:max-content}
.panel-box .rule{width:26px;height:2px;margin:10px auto 0}
.panel-box p{font-size:8.5px;line-height:16px;margin-top:10px;padding:0 12px}
.box-left{left:65px}
.box-left h2{color:var(--white);background:#3f2f28}
.box-left .rule{background:var(--white)}
.box-left p{color:var(--white);padding:0 45px}
.box-right{left:416px}
.box-right h2{color:var(--ink);background:#e4e6e8}
.box-right .rule{background:var(--blue)}

/* call now */
.callnow-bar{left:66px;top:931px;width:2px;height:32px;background:var(--ink)}
.callnow-title{left:78px;top:928px;font-family:'Cinzel',serif;font-size:18px;color:var(--ink)}
.callnow-sub{left:79px;top:952px;font-size:8.5px}
.callnow-arrow{left:434px;top:941px}
.callnow-box{left:502px;top:928px;width:224px;height:40px;border-top:1px solid #ddd;border-bottom:1px solid #ddd;display:flex;align-items:center;padding-left:22px;gap:14px}
.callnow-box strong{font-family:'Cinzel',serif;font-weight:400;font-size:22px}

/* footer */
.site-footer{left:0;top:1000px;width:792px;height:165px;background:var(--slate)}
.footer-title{left:74px;top:1036px;color:var(--white);font-family:'Cinzel',serif;font-size:15px;letter-spacing:.5px}
.contact-item{left:76px;display:flex;gap:8px;color:var(--white);font-size:9px;line-height:13.5px}
.contact-item svg{flex:none;margin-top:1px}
.map{left:338px;top:1034px;width:322px;height:97px;border-radius:3px;background:linear-gradient(135deg,#8fc9e3,#b7dcc0 45%,#e9e4d4 70%,#9fd1e8)}
.map-link{left:339px;top:1136px;color:var(--white);font-size:8px;font-weight:700;display:flex;align-items:center;gap:4px}
.copyright{left:0;top:1165px;width:792px;height:35px;background:var(--slate-deep);color:var(--muted);font-size:9px;text-align:center;line-height:35px}
.copyright b{color:var(--white)}
</style>
</head>
<body>

<header class="site-header abs"></header>
<div class="brand abs"><span class="brand-mark"></span><span class="brand-name">HARBORLINE LAW GROUP</span></div>
<div class="header-call abs">
  <svg width="26" height="26" viewBox="0 0 26 26"><circle cx="13" cy="13" r="11.5" fill="none" stroke="#1c1c1c" stroke-width="2"/><path d="M9 8c1-1 2-1 2.5 0l1 2c.3.7 0 1.2-.6 1.6l-.6.4c.6 1.4 1.6 2.5 3 3.2l.5-.6c.4-.5 1-.7 1.6-.4l2 1c.9.4 1 1.5.1 2.4-1.2 1.2-3 1.3-5 0-2.3-1.5-4-3.5-4.8-5.8C8.3 10.300 8.300 9 9 8z" fill="#1c1c1c"/></svg>
  <div><small>CALL US NOW!</small><strong>555-240-7190</strong></div>
</div>

<section>
  <div class="hero abs" role="img" aria-label="Photo of a lawyer consulting with an injured elderly client and his wife"></div>
  <div class="hero-shade abs"></div>
  <div class="slide-tab abs"><i></i><i></i><i></i></div>
  <p class="hero-kicker abs">ACCIDENT? INJURED?</p>
  <h1 class="hero-title abs" style="font-weight:400">YOUR CASE YOUR MONEY</h1>
  <div class="hero-btn abs">
    <svg width="16" height="16" viewBox="0 0 26 26"><circle cx="13" cy="13" r="11.5" fill="none" stroke="#fff" stroke-width="2"/><path d="M9 8c1-1 2-1 2.5 0l1 2c.3.7 0 1.2-.6 1.6l-.6.4c.6 1.4 1.6 2.5 3 3.2l.5-.6c.4-.5 1-.7 1.6-.4l2 1c.9.4 1 1.5.1 2.4-1.2 1.2-3 1.3-5 0-2.3-1.5-4-3.5-4.8-5.8C8.3 10.3 8.3 9 9 8z" fill="#fff"/></svg>
    CALL: <span>555-240-7190</span>
  </div>
  <svg class="scroll-cue abs" width="14" height="28" viewBox="0 0 14 28"><rect x="3" y="1" width="8" height="14" rx="4" fill="none" stroke="#fff" stroke-width="1.2"/><line x1="7" y1="4" x2="7" y2="7" stroke="#fff" stroke-width="1.2"/><path d="M3 18l4 3 4-3M3 22l4 3 4-3" fill="none" stroke="#fff" stroke-width="1"/></svg>
</section>

<section>
  <div class="feature abs" style="left:30px">
    <div class="feature-icon" role="img" aria-label="Money icon"></div><div class="feature-shadow"></div>
    <h3>LOW FEES</h3><p>We charge less, so you<br>keep more.</p>
  </div>
  <div class="feature abs" style="left:189px">
    <div class="feature-icon" role="img" aria-label="Meeting icon"></div><div class="feature-shadow"></div>
    <h3>FREE<br>CONSULTATION</h3><p>It's always free to talk<br>to us.</p>
  </div>
  <div class="feature abs" style="left:372px">
    <div class="feature-icon" role="img" aria-label="Touch screen icon"></div><div class="feature-shadow"></div>
    <h3>GET STARTED USING ONLY<br>YOUR PHONE</h3><p>No need to come to the office,<br>sign up using your phone.</p>
  </div>
  <div class="feature abs" style="left:570px">
    <div class="feature-icon" role="img" aria-label="Lawyer speaking icon"></div><div class="feature-shadow"></div>
    <h3>SPEAK DIRECTLY<br>TO A LAWYER</h3><p>No staff screening. Talk right<br>to a lawyer on your first call.</p>
  </div>
</section>

<section>
  <div class="cta-band abs"></div>
  <div class="cta-band bar abs" style="top:611px;height:30px;width:2px;background:#fff;left:66px"></div>
  <p class="cta-band-text abs">CALL&nbsp; NOW&nbsp; FOR FREE CONSULTATION :</p>
  <svg class="cta-band-icon abs" width="36" height="36" viewBox="0 0 26 26"><circle cx="13" cy="13" r="11.5" fill="none" stroke="#fff" stroke-width="1.6"/><path d="M9 8c1-1 2-1 2.5 0l1 2c.3.7 0 1.2-.6 1.6l-.6.4c.6 1.4 1.6 2.5 3 3.2l.5-.6c.4-.5 1-.7 1.6-.4l2 1c.9.4 1 1.5.1 2.4-1.2 1.2-3 1.3-5 0-2.3-1.5-4-3.5-4.8-5.8C8.3 10.3 8.3 9 9 8z" fill="#fff"/></svg>
  <p class="cta-band-num abs">555-240-7190</p>
</section>

<section>
  <div class="panel-left abs" role="img" aria-label="Blurred photo of attorneys in a law library"></div>
  <div class="panel-right abs" role="img" aria-label="Blurred photo of a client meeting in a bright office"></div>
  <div class="panel-box box-left abs">
    <h2>NO FEE UNLESS WE WIN</h2><div class="rule"></div>
    <p>We don't get paid unless you get paid. It's as simple as that. We let our results do the talking for us.</p>
  </div>
  <div class="panel-box box-right abs">
    <h2>QUESTIONS ABOUT ANYTHING?</h2><div class="rule"></div>
    <p>We're here to help. Feel free to call us at 555-240-7190 to speak to one of our attorneys. With extensive experience in helping clients get the results that they want, our team is always just a phone call away.</p>
  </div>
</section>

<section>
  <div class="callnow-bar abs"></div>
  <p class="callnow-title abs">CALL US&nbsp; NOW!</p>
  <p class="callnow-sub abs">Lorem ipsum dolor sit amet, consectetuer adipiscing elit, sed diam nonummy nibh</p>
  <svg class="callnow-arrow abs" width="40" height="16" viewBox="0 0 40 16"><path d="M1 10c12 0 24-2 36-6" fill="none" stroke="#1c1c1c" stroke-width="1.2"/><path d="M30 3l7 1-4 6" fill="none" stroke="#1c1c1c" stroke-width="1.2"/></svg>
  <div class="callnow-box abs">
    <svg width="28" height="28" viewBox="0 0 26 26"><circle cx="13" cy="13" r="11.5" fill="none" stroke="#1c1c1c" stroke-width="1.6"/><path d="M9 8c1-1 2-1 2.5 0l1 2c.3.7 0 1.2-.6 1.6l-.6.4c.6 1.4 1.6 2.5 3 3.2l.5-.6c.4-.5 1-.7 1.6-.4l2 1c.9.4 1 1.5.1 2.4-1.2 1.2-3 1.3-5 0-2.3-1.5-4-3.5-4.8-5.800C8.3 10.3 8.3 9 9 8z" fill="#1c1c1c"/></svg>
    <strong>555-240-7190</strong>
  </div>
</section>

<footer>
  <div class="site-footer abs"></div>
  <h2 class="footer-title abs" style="font-weight:400">CONTACT INFO</h2>
  <div class="contact-item abs" style="top:1063px">
    <svg width="10" height="14" viewBox="0 0 10 14"><path d="M5 0a5 5 0 0 1 5 5c0 3.5-5 9-5 9S0 8.5 0 5a5 5 0 0 1 5-5z" fill="#fff"/><circle cx="5" cy="5" r="2" fill="#353a45"/></svg>
    <div><b>Harborline Law Group</b><br>Riverside Office Suite<br>Lakeview, LA 70019</div>
  </div>
  <div class="contact-item abs" style="top:1110px">
    <svg width="10" height="10" viewBox="0 0 10 10"><path d="M2 0.500c.8-.5 1.500 0 1.800.7l.6 1.300c.2.5 0 .9-.4 1.200l-.5.4c.5 1.100 1.300 1.900 2.300 2.400l.4-.5c.3-.4.8-.5 1.200-.3l1.300.6c.7.3.9 1.100.3 1.800C8.200 9.400 6.800 9.700 5 8.500 3.200 7.300 1.800 5.700 1 3.800.500 2.500.900 1.200 2 .5z" fill="#fff"/></svg>
    <div><b>555-240-7190</b></div>
  </div>
  <div class="contact-item abs" style="top:1129px">
    <svg width="11" height="8" viewBox="0 0 11 8"><rect width="11" height="8" fill="#fff"/><path d="M0 0l5.5 4.500L11 0" fill="none" stroke="#353a45" stroke-width="1"/></svg>
    <div>info@harborlinelaw.com</div>
  </div>
  <div class="map abs" role="img" aria-label="Street map showing the office location"></div>
  <div class="map-link abs">View Full Map
    <svg width="10" height="6" viewBox="0 0 10 6"><path d="M0 3h8M6 1l2 2-2 2" fill="none" stroke="#fff" stroke-width="1.2"/></svg>
  </div>
  <p class="copyright abs">Copyright © 2016 <b>Harborline Law Group</b> &nbsp;I&nbsp; All Rights Reserved.</p>
</footer>

</body>
</html>
```